Artisan Bread Company Needs a Poster

We need a poster design (with the measurements 1 Ft Horizontal, by 2 Ft Vertical) This poster is to advertise "Morrow's Loaf" and draw attention to the new product. The poster MUST have the "Morrow's Loaf Logo" provided below. (Signage.ai) The lettering below that says "local, organic, sourdough" can be moved around. It must be somewhere on the poster though. The poster is to inform people that the bread is Organic, local, and sourdough.
Feel free to use any pictures that would work.
The poster should have the text-- "Morrow's Loaf is made from 100% Organic flour, grown and milled in Ontario. Morrow's Loaf uses a traditional sourdough method with a long fermentation time, to help with digestibility. All of our breads are hand shaped, and hearth baked in a scorching hot oven."
Target Market(s)
People conscious about their eating habits, anywhere from 24-60. Think yoga moms.
Industry/Entity Type
Bakery
Requirements
Must have
- The poster MUST have the "Morrow's Loaf Logo" provided below. (Signage.ai) The lettering below that says "local, organic, sourdough" can be moved around. It must be somewhere on the poster though. The poster is to inform people that the bread is Organic, local, and sourdough.

```html
<!DOCTYPE html>
<html lang="en">
<head>
<meta charset="utf-8">
<title>Morrow's Loaf – Local, Organic, Sourdough</title>
<link rel="stylesheet" href="https://fonts.googleapis.com/css2?family=Great+Vibes&family=Noto+Serif&display=swap">
<style>
  :root {
    --paper: #ffffff;
    --ink: #1a1a1a;
    --local: #f07272;
    --organic: #67b14b;
    --sourdough: #e3b93d;
    --crust-dark: #6b4322;
    --crust: #a9743f;
    --flour: #d9c8ad;
    --script: "Great Vibes", cursive;
    --body: "Noto Serif", serif;
  }
  html, body {
    margin: 0;
    padding: 0;
    width: 1200px;
    height: 2400px;
    overflow: hidden;
    background: var(--paper);
  }
  .poster {
    position: relative;
    width: 1200px;
    height: 2400px;
    background: var(--paper);
    overflow: hidden;
  }
  .brand {
    position: absolute;
    top: 150px;
    left: 0;
    width: 1200px;
    margin: 0;
    text-align: center;
    font-family: var(--script);
    font-weight: 400;
    font-size: 190px;
    line-height: 1;
    color: var(--ink);
  }
  .claim {
    position: absolute;
    left: 283px;
    width: 917px;
    display: flex;
    align-items: center;
    padding-left: 70px;
    box-sizing: border-box;
    font-family: var(--script);
    font-size: 112px;
    color: var(--paper);
    line-height: 1;
  }
  .claim--local { top: 547px; height: 178px; background: var(--local); }
  .claim--organic { top: 799px; height: 185px; background: var(--organic); }
  .claim--sourdough { top: 1068px; height: 182px; background: var(--sourdough); }
  .claim-icon {
    position: absolute;
    left: 100px;
    width: 104px;
    height: 104px;
  }
  .claim-icon--local { top: 585px; }
  .claim-icon--organic { top: 840px; }
  .claim-icon--sourdough { top: 1105px; }
  .story {
    position: absolute;
    top: 1342px;
    left: 281px;
    width: 760px;
    margin: 0;
    font-family: var(--body);
    font-size: 22.5px;
    line-height: 27px;
    color: var(--ink);
  }
  .bread-photo {
    position: absolute;
    left: 0;
    top: 1740px;
    width: 1200px;
    height: 660px;
    background:
      radial-gradient(ellipse 40% 55% at 35% 55%, var(--crust) 0%, rgba(169,116,63,0) 70%),
      radial-gradient(ellipse 35% 50% at 75% 60%, var(--flour) 0%, rgba(217,200,173,0) 70%),
      linear-gradient(180deg, rgba(107,67,34,0) 0%, var(--crust-dark) 30%, var(--crust) 65%, var(--crust-dark) 100%);
  }
  .float-icon { position: absolute; }
  .float-icon--house { left: 62px; top: 1705px; width: 80px; height: 80px; }
  .float-icon--wheat { left: 860px; top: 1715px; width: 120px; height: 90px; }
  .float-icon--leaf { left: 1100px; top: 1850px; width: 80px; height: 100px; }
</style>
</head>
<body>
<main class="poster">
  <h1 class="brand">Morrow's Loaf</h1>

  <svg class="claim-icon claim-icon--local" viewBox="0 0 100 100" aria-hidden="true">
    <path d="M12 44 L50 14 L88 44 L88 88 L12 88 Z" fill="none" stroke="var(--local)" stroke-width="7" stroke-linejoin="round"/>
    <rect x="40" y="58" width="20" height="30" fill="var(--local)"/>
  </svg>
  <div class="claim claim--local">-Local-</div>

  <svg class="claim-icon claim-icon--organic" viewBox="0 0 100 100" aria-hidden="true">
    <path d="M14 90 C10 50 40 14 88 10 C90 56 60 88 14 90 Z" fill="none" stroke="var(--organic)" stroke-width="7" stroke-linejoin="round"/>
    <path d="M14 90 L64 36" fill="none" stroke="var(--organic)" stroke-width="6" stroke-linecap="round"/>
  </svg>
  <div class="claim claim--organic">-Organic-</div>

  <svg class="claim-icon claim-icon--sourdough" viewBox="0 0 100 100" aria-hidden="true">
    <g fill="var(--sourdough)">
      <path d="M56 96 L40 20" stroke="var(--sourdough)" stroke-width="6" stroke-linecap="round"/>
      <ellipse cx="38" cy="12" rx="6" ry="11"/>
      <ellipse cx="30" cy="34" rx="6" ry="12" transform="rotate(-35 30 34)"/>
      <ellipse cx="54" cy="30" rx="6" ry="12" transform="rotate(35 54 30)"/>
      <ellipse cx="34" cy="54" rx="6" ry="12" transform="rotate(-35 34 54)"/>
      <ellipse cx="58" cy="50" rx="6" ry="12" transform="rotate(35 58 50)"/>
      <ellipse cx="38" cy="74" rx="6" ry="12" transform="rotate(-35 38 74)"/>
      <ellipse cx="62" cy="70" rx="6" ry="12" transform="rotate(35 62 70)"/>
    </g>
  </svg>
  <div class="claim claim--sourdough">-Sourdough-</div>

  <p class="story">Morrow's Loaf is made from 100% Organic flour, grown<br>and milled in Ontario. Morrow's Loaf uses a traditional<br>sourdough method with a long fermentation time, to help<br>with digestibility. All of our breads are hand shaped, and<br>hearth baked in a scorching hot oven</p>

  <div class="bread-photo" role="img" aria-label="Pile of rustic hand-shaped sourdough loaves with floured, scored crusts"></div>

  <svg class="float-icon float-icon--house" viewBox="0 0 100 100" aria-hidden="true">
    <path d="M14 46 L46 16 L86 40 L80 86 L14 80 Z" fill="none" stroke="var(--local)" stroke-width="7" stroke-linejoin="round"/>
    <rect x="40" y="56" width="18" height="26" fill="var(--local)"/>
  </svg>
  <svg class="float-icon float-icon--wheat" viewBox="0 0 120 90" aria-hidden="true">
    <g fill="var(--sourdough)">
      <path d="M8 84 L96 18" stroke="var(--sourdough)" stroke-width="5" stroke-linecap="round"/>
      <ellipse cx="104" cy="12" rx="11" ry="6" transform="rotate(-35 104 12)"/>
      <ellipse cx="78" cy="22" rx="6" ry="12" transform="rotate(20 78 22)"/>
      <ellipse cx="90" cy="40" rx="6" ry="12" transform="rotate(80 90 40)"/>
      <ellipse cx="56" cy="38" rx="6" ry="12" transform="rotate(20 56 38)"/>
      <ellipse cx="68" cy="56" rx="6" ry="12" transform="rotate(80 68 56)"/>
      <ellipse cx="34" cy="54" rx="6" ry="12" transform="rotate(20 34 54)"/>
      <ellipse cx="46" cy="72" rx="6" ry="12" transform="rotate(80 46 72)"/>
    </g>
  </svg>
  <svg class="float-icon float-icon--leaf" viewBox="0 0 80 100" aria-hidden="true">
    <path d="M40 94 C10 70 12 30 44 6 C72 34 68 72 40 94 Z" fill="none" stroke="var(--organic)" stroke-width="6" stroke-linejoin="round"/>
    <path d="M40 94 L44 40" fill="none" stroke="var(--organic)" stroke-width="5" stroke-linecap="round"/>
  </svg>
</main>
</body>
</html>
```